Flyer KLV 30 Jahre
Sehr gute Kommunikation. Unser Briefing wurde kreativ und achtsam umgesetzt. Wirklich eine angenehme Zusammenarbeit!
Zielgruppe
Wir begleiten Menschen mit Lernschwierigkeiten, seelischen Behinderungen oder als Familien mit Unterstützungsbedarf zu einer selbstbestimmten Teilhabe am gesellschaftlichen Leben.
Aufgabenstellung
siehe Datei Flyerkonzept

```html
<!DOCTYPE html>
<html lang="de">
<head>
<meta charset="utf-8">
<title>LUMERA e.V. – Flyer</title>
<link rel="stylesheet" href="https://fonts.googleapis.com/css2?family=Open+Sans:wght@400;600;700&display=swap">
<style>
  :root {
    --bg: #c9c8c9;
    --paper: #ffffff;
    --brand-blue: #1d6b8e;
    --brand-green: #5fa466;
    --text-blue: #1f6a8a;
    --photo-light: #fbf7f2;
    --photo-warm: #efb27e;
    --photo-deep: #8a6a4e;
  }
  * { margin: 0; padding: 0; box-sizing: border-box; }
  html, body { width: 1200px; height: 800px; overflow: hidden; }
  body {
    background: var(--bg);
    font-family: "Open Sans", Arial, sans-serif;
    display: flex;
    align-items: center;
    justify-content: center;
  }
  .spread {
    display: flex;
    width: 960px;
    height: 680px;
    background: var(--paper);
    box-shadow: 0 12px 30px rgba(0,0,0,0.18);
  }
  .panel {
    position: relative;
    width: 480px;
    height: 680px;
    overflow: hidden;
    background: var(--paper);
  }
  .panel--back { border-right: 1px solid #e4e4e4; }
  .stripe { position: absolute; left: 0; right: 0; }
  .stripe--blue { top: 0; height: 34px; background: var(--brand-blue); }
  .stripe--green { top: 34px; height: 30px; background: var(--brand-green); }

  .contact {
    position: absolute;
    top: 100px; left: 0; right: 0;
    text-align: center;
    color: var(--text-blue);
    font-size: 22px;
    line-height: 1.3;
    letter-spacing: 0.5px;
  }
  .contact__org { font-weight: 700; font-size: 21px; margin-bottom: 6px; }
  .contact__block + .contact__block { margin-top: 22px; }

  .claim {
    position: absolute;
    left: 0; right: 0;
    height: 44px;
    background: var(--brand-blue);
    color: var(--paper);
    font-size: 24px;
    font-weight: 600;
    letter-spacing: 1px;
    display: flex;
    align-items: center;
    justify-content: center;
  }
  .panel--back .claim { top: 356px; }
  .panel--front .claim { top: 318px; }

  .photo {
    position: absolute;
    left: 0; right: 0; bottom: 0;
    background: linear-gradient(160deg, var(--photo-light) 0%, var(--photo-warm) 45%, var(--photo-deep) 100%);
  }
  .panel--back .photo { top: 400px; }
  .panel--front .photo { top: 362px; }

  .brand {
    position: absolute;
    top: 175px; left: 0; right: 0;
    display: flex;
    align-items: center;
    justify-content: center;
    gap: 18px;
  }
  .brand__dot {
    width: 30px; height: 30px;
    border-radius: 50%;
    background: var(--brand-green);
  }
  .brand__name {
    color: var(--brand-blue);
    font-size: 68px;
    font-weight: 400;
    letter-spacing: 6px;
  }
</style>
</head>
<body>
  <main class="spread">
    <section class="panel panel--back">
      <div class="stripe stripe--blue"></div>
      <div class="stripe stripe--green"></div>
      <address class="contact" style="font-style: normal;">
        <div class="contact__block">
          <div class="contact__org">LUMERA e.V.</div>
          <div>Lindenhofweg 7</div>
          <div>10115 Berlin</div>
        </div>
        <div class="contact__block">
          <div>Tel.: 030 - 412 388 0</div>
          <div>Fax: 030 - 412 388 19</div>
        </div>
        <div class="contact__block">
          <div>E-Mail: info@lumera-berlin.de</div>
          <div>Web: www.lumera-berlin.de</div>
        </div>
      </address>
      <div class="claim">Wir begleiten Menschen</div>
      <div class="photo" role="img" aria-label="Foto: eine Gruppe junger Menschen von hinten, Arm in Arm, im warmen Gegenlicht"></div>
    </section>

    <section class="panel panel--front">
      <div class="stripe stripe--blue"></div>
      <div class="stripe stripe--green"></div>
      <div class="brand">
        <span class="brand__dot"></span>
        <span class="brand__name">LUMERA</span>
      </div>
      <div class="claim">Wir begleiten Menschen</div>
      <div class="photo" role="img" aria-label="Foto: Freunde von hinten, die sich gegenseitig umarmen, im hellen Sonnenlicht"></div>
    </section>
  </main>
</body>
</html>
```